I am a highly experienced private practice psychotherapist serving high end clientele in the Wall Street area of New York City. I need electronic letterhead (that can also be printed) to use for bills, receipts, and correspondences.

My clients are very high end and are used to elegance and wealth. The letterhead should contain the following information: Marian T. Holcombe, LCSW 72 Pellham Street, Suite 2561 New York, NY 10087 Phone : (917) 555-3194 email: therapy@marianholcombelcsw.example website: www.marianholcombelcsw.example

Thank you for your designs. Please be advised that the letterhead will be used for bills/invoices; professional letters to other mental health professionals and doctors, as well as to attorneys. It needs to be highly professional in the same way that a law firm has professional and elegant letterhead, raher than whimsical or with spa designers. My letters end up as official documents.

```html
<!DOCTYPE html>
<html lang="en">
<head>
<meta charset="utf-8">
<title>Marian Holcombe LCSW Psychotherapy – Letterhead</title>
<link rel="stylesheet" href="https://fonts.googleapis.com/css2?family=Tinos:wght@700&family=Roboto+Condensed:wght@400;700&display=swap">
<style>
  :root {
    --paper: #ffffff;
    --ink: #2a2a2a;
    --band-green-light: #7cc24a;
    --band-green: #3f7f2a;
    --band-mat: #4a525b;
    --band-mat-dark: #262b31;
    --name-white: #ffffff;
    --base-bar: #1c1c1c;
  }
  * { margin: 0; padding: 0; box-sizing: border-box; }
  html, body { width: 846px; height: 1200px; overflow: hidden; background: var(--paper); }
  .letterhead { position: relative; width: 846px; height: 1200px; background: var(--paper); }

  .masthead { position: absolute; left: 0; top: 0; width: 846px; height: 120px; }
  .masthead-scene {
    position: absolute; inset: 0;
    background: linear-gradient(180deg, var(--band-green-light) 0%, var(--band-green) 24%, var(--band-mat) 28%, var(--band-mat-dark) 100%);
  }
  .practice-name {
    position: absolute; right: 32px; top: 34px;
    font-family: "Tinos", "Times New Roman", serif; font-weight: 700;
    font-size: 46px; line-height: 1; letter-spacing: 6px;
    color: var(--name-white);
  }
  .practice-title {
    position: absolute; right: 32px; top: 88px;
    font-family: "Roboto Condensed", Arial, sans-serif; font-weight: 700;
    font-size: 15px; line-height: 1; letter-spacing: 8.2px;
    color: var(--name-white);
  }

  .contact {
    position: absolute; left: 184px; top: 1138px; width: 476px;
    font-family: "Roboto Condensed", Arial, sans-serif; font-weight: 400;
    font-size: 13px; line-height: 19px; color: var(--ink);
  }
  .contact-address { text-align: justify; text-align-last: justify; }
  .contact-online { white-space: nowrap; letter-spacing: -0.15px; }

  .base-bar { position: absolute; left: 0; bottom: 0; width: 846px; height: 19px; background: var(--base-bar); }
</style>
</head>
<body>
  <main class="letterhead">
    <header class="masthead">
      <div class="masthead-scene" role="img" aria-label="Header photograph area: calm still-life in green and charcoal tones"></div>
      <h1 class="practice-name">Marian Holcombe</h1>
      <p class="practice-title">LCSW Psychotherapy</p>
    </header>

    <footer class="contact">
      <p class="contact-address">72 Pellham Street, Suite 2561 New York, NY 10087, Phone : (917) 555-3194</p>
      <p class="contact-online">email : therapy@marianholcombelcsw.example , website : www.marianholcombelcsw.example</p>
    </footer>
    <div class="base-bar"></div>
  </main>
</body>
</html>
```